Helicopter company requires newspaper ad

"Ridgeline Aviation" is an agricultural helicopter company based in Victoria, Australia. We need an advert design for use in newspapers and also possibly social media. Our company specialises in using a helicopter for various agricultural work such as Spraying weeds ("Cropdusting"), spreading fertiliser. This advert will be targeted at farmers in our service area, Our customers are mainly dairy and cow farmers and our services are aimed at increasing their farm productivity. The final design should inform potential and existing customers about our services and the benefits of them. I will attach files of our logo and some existing advertising material for guidance. We would like the ad to feature the blue and green colours in our logo Please feel free to view our website and facebook page to see more about what we do. www.ridgelineaviation.com.au Some text we would like included Spraying: -Accurate -Time Efficient -Zero crop damage -Cost efficient Fertiliser Spreading: -Accurate, Pattern-tested equipment -Zero crop damage or wheel marks -Ability to load product out of a truck, bin or bulk bags -Cost effective, Prices from $32 per hectare depending on spread rate The final advert size should be 195 mm wide x 186 mm high Thanks :)

Farmers, Agriculture Industry

Agribusiness

Designer to choose colors to be used in the design.

• Phone number 0491 736 058
• The text included in the decription, or variations of this

```html
<!DOCTYPE html>
<html lang="en">
<head>
<meta charset="utf-8">
<title>Ridgeline Aviation – Summer Crops Ad</title>
<link rel="stylesheet" href="https://fonts.googleapis.com/css2?family=Montserrat:wght@700;800&family=Lato:wght@400;700;900&display=swap">
<style>
  :root {
    --brand-green: #1f8f3c;
    --field-green: #5aab3d;
    --field-green-light: #8cc63f;
    --brand-blue: #1a73c9;
    --badge-blue: #2281d6;
    --sky-top: #ffffff;
    --sky-mid: #cfe0ee;
    --hill: #8c9b74;
    --ink: #1b1b1b;
    --white: #ffffff;
  }
  * { margin: 0; padding: 0; box-sizing: border-box; }
  html, body { width: 1200px; height: 1104px; overflow: hidden; background: #ffffff; }
  .ad {
    position: relative;
    width: 1200px;
    height: 1104px;
    overflow: hidden;
    font-family: "Lato", Arial, sans-serif;
    color: var(--white);
  }
  .ad__art { position: absolute; inset: 0; }
  .headline {
    position: absolute;
    left: 45px;
    top: 48px;
    font-family: "Montserrat", Arial, sans-serif;
    font-weight: 800;
    font-size: 44px;
    line-height: 58px;
    color: var(--brand-green);
    letter-spacing: 0.5px;
  }
  .brand-name {
    position: absolute;
    right: 48px;
    top: 78px;
    width: 300px;
    text-align: right;
    font-family: "Montserrat", Arial, sans-serif;
    font-weight: 800;
    font-size: 38px;
    line-height: 42px;
    color: var(--brand-blue);
  }
  .badge-text {
    position: absolute;
    left: 911px;
    top: 487px;
    width: 250px;
    text-align: center;
    font-size: 24px;
    line-height: 40px;
    color: var(--white);
  }
  .badge-text strong { font-weight: 900; font-size: 25px; }
  .service {
    position: absolute;
    top: 708px;
  }
  .service--spreading { left: 45px; }
  .service--spraying { left: 750px; }
  .service__title {
    font-family: "Montserrat", Arial, sans-serif;
    font-weight: 800;
    font-size: 31px;
    line-height: 42px;
    margin-bottom: 4px;
  }
  .benefits { list-style: none; }
  .benefits li {
    display: flex;
    align-items: center;
    gap: 10px;
    font-size: 22px;
    line-height: 38px;
  }
  .benefits svg { width: 24px; height: 24px; flex: none; }
  .price-note {
    position: absolute;
    left: 45px;
    top: 982px;
    font-size: 22px;
    line-height: 31px;
  }
  .price-note strong { font-weight: 900; }
  .contact {
    position: absolute;
    right: 45px;
    top: 966px;
    text-align: right;
    font-style: normal;
  }
  .contact__tagline {
    font-weight: 900;
    font-size: 22px;
    color: var(--brand-blue);
    line-height: 36px;
  }
  .contact__line {
    display: flex;
    justify-content: flex-end;
    align-items: center;
    gap: 14px;
    color: var(--ink);
    line-height: 44px;
  }
  .contact__phone { font-weight: 900; font-size: 29px; letter-spacing: 0.5px; }
  .contact__web { font-size: 27px; }
  .contact__line svg { width: 28px; height: 28px; flex: none; }
</style>
</head>
<body>
<main class="ad">
  <svg class="ad__art" viewBox="0 0 1200 1104" width="1200" height="1104">
    <defs>
      <linearGradient id="scene-fill" x1="0" y1="0" x2="0" y2="1">
        <stop offset="0" stop-color="#ffffff"/>
        <stop offset="0.18" stop-color="#f2f6fa"/>
        <stop offset="0.45" stop-color="#cfe0ee"/>
        <stop offset="0.58" stop-color="#e6ecef"/>
        <stop offset="0.68" stop-color="#8c9b74"/>
        <stop offset="1" stop-color="#6f8a4a"/>
      </linearGradient>
      <radialGradient id="field-fill" cx="0.55" cy="0.3" r="0.7">
        <stop offset="0" stop-color="#8cc63f"/>
        <stop offset="1" stop-color="#5aab3d"/>
      </radialGradient>
    </defs>

    <rect class="scene-photo" x="0" y="0" width="1200" height="720" fill="url(#scene-fill)"
          role="img" aria-label="Photo of a helicopter spraying a green pasture with rolling hills and a cloudy sky"/>

    <path class="wave-white" d="M0,598 C320,686 720,704 1200,548 L1200,1104 L0,1104 Z" fill="var(--white)"/>
    <path class="wave-blue" d="M0,606 C320,696 720,712 1200,556 L1200,1104 L0,1104 Z" fill="var(--brand-blue)"/>
    <path class="field" d="M0,640 C320,726 720,736 1200,586 L1200,1104 L0,1104 Z" fill="url(#field-fill)"/>

    <path class="footer-blue" d="M440,1104 C600,990 860,930 1200,918 L1200,1104 Z" fill="var(--brand-blue)"/>
    <path class="footer-white" d="M470,1104 C620,1004 870,946 1200,934 L1200,1104 Z" fill="var(--white)"/>

    <g class="price-badge" transform="translate(1036 582) scale(1.25)">
      <polygon fill="var(--badge-blue)" points="100,0 88.3,17.6 92.4,38.3 74.8,50 70.7,70.7 50,74.8 38.3,92.4 17.6,88.3 0,100 -17.6,88.3 -38.3,92.4 -50,74.8 -70.7,70.7 -74.8,50 -92.4,38.3 -88.3,17.6 -100,0 -88.3,-17.6 -92.4,-38.3 -74.8,-50 -70.7,-70.7 -50,-74.8 -38.3,-92.4 -17.6,-88.3 0,-100 17.6,-88.3 38.3,-92.4 50,-74.8 70.7,-70.7 74.8,-50 92.4,-38.3 88.3,-17.6"/>
    </g>
  </svg>

  <h1 class="headline">SUMMER CROPS NEED<br>SPRAYING OR FERTILISER?</h1>

  <div class="brand-name">Ridgeline Aviation</div>

  <p class="badge-text">Prices from<br><strong>$32 PER HECTARE</strong><br>depending on<br>spread rate</p>

  <section class="service service--spreading">
    <h2 class="service__title">SPREADING</h2>
    <ul class="benefits">
      <li><svg viewBox="0 0 24 24"><circle cx="12" cy="12" r="10" fill="none" stroke="#fff" stroke-width="1.8"/><path d="M7.5 12.5l3 3 6-6.5" fill="none" stroke="#fff" stroke-width="2" stroke-linecap="round" stroke-linejoin="round"/></svg>Accurate</li>
      <li><svg viewBox="0 0 24 24"><circle cx="12" cy="12" r="10" fill="none" stroke="#fff" stroke-width="1.8"/><path d="M7.5 12.5l3 3 6-6.5" fill="none" stroke="#fff" stroke-width="2" stroke-linecap="round" stroke-linejoin="round"/></svg>Pattern-tested equipment</li>
      <li><svg viewBox="0 0 24 24"><circle cx="12" cy="12" r="10" fill="none" stroke="#fff" stroke-width="1.8"/><path d="M7.5 12.5l3 3 6-6.5" fill="none" stroke="#fff" stroke-width="2" stroke-linecap="round" stroke-linejoin="round"/></svg>Zero crop damage or wheel marks</li>
      <li><svg viewBox="0 0 24 24"><circle cx="12" cy="12" r="10" fill="none" stroke="#fff" stroke-width="1.8"/><path d="M7.5 12.5l3 3 6-6.5" fill="none" stroke="#fff" stroke-width="2" stroke-linecap="round" stroke-linejoin="round"/></svg>Ability to load product out of a truck, bin or bulk bags</li>
      <li><svg viewBox="0 0 24 24"><circle cx="12" cy="12" r="10" fill="none" stroke="#fff" stroke-width="1.8"/><path d="M7.5 12.5l3 3 6-6.5" fill="none" stroke="#fff" stroke-width="2" stroke-linecap="round" stroke-linejoin="round"/></svg>Cost effective</li>
    </ul>
  </section>

  <section class="service service--spraying">
    <h2 class="service__title">SPRAYING</h2>
    <ul class="benefits">
      <li><svg viewBox="0 0 24 24"><circle cx="12" cy="12" r="10" fill="none" stroke="#fff" stroke-width="1.8"/><path d="M7.5 12.5l3 3 6-6.5" fill="none" stroke="#fff" stroke-width="2" stroke-linecap="round" stroke-linejoin="round"/></svg>Accurate</li>
      <li><svg viewBox="0 0 24 24"><circle cx="12" cy="12" r="10" fill="none" stroke="#fff" stroke-width="1.8"/><path d="M7.5 12.5l3 3 6-6.5" fill="none" stroke="#fff" stroke-width="2" stroke-linecap="round" stroke-linejoin="round"/></svg>Time Efficient</li>
      <li><svg viewBox="0 0 24 24"><circle cx="12" cy="12" r="10" fill="none" stroke="#fff" stroke-width="1.8"/><path d="M7.5 12.5l3 3 6-6.5" fill="none" stroke="#fff" stroke-width="2" stroke-linecap="round" stroke-linejoin="round"/></svg>Zero crop damage</li>
      <li><svg viewBox="0 0 24 24"><circle cx="12" cy="12" r="10" fill="none" stroke="#fff" stroke-width="1.8"/><path d="M7.5 12.5l3 3 6-6.5" fill="none" stroke="#fff" stroke-width="2" stroke-linecap="round" stroke-linejoin="round"/></svg>Cost efficient Fertiliser</li>
    </ul>
  </section>

  <p class="price-note">Prices from <strong>$32</strong> per hectare depending<br>on spread rate</p>

  <address class="contact">
    <div class="contact__tagline">Aerial Agriculture Specialists</div>
    <div class="contact__line contact__phone">0491 736 058
      <svg viewBox="0 0 28 28"><circle cx="14" cy="14" r="13" fill="var(--brand-blue)"/><path d="M10 7.5c.6-.4 1.3-.2 1.6.4l1.2 2.4c.3.6.1 1.2-.4 1.6l-.9.6c.6 1.6 1.8 3 3.3 3.8l.7-.8c.4-.5 1.1-.6 1.6-.3l2.3 1.3c.6.3.8 1.1.4 1.6l-.8 1.1c-.6.8-1.6 1.1-2.5.8-4-1.3-7-4.6-8-8.6-.2-.9.1-1.8.8-2.3z" fill="#fff"/></svg>
    </div>
    <div class="contact__line contact__web">www.ridgelineaviation.com.au
      <svg viewBox="0 0 28 28"><circle cx="14" cy="14" r="13" fill="var(--brand-blue)"/><circle cx="14" cy="14" r="7.5" fill="none" stroke="#fff" stroke-width="1.5"/><ellipse cx="14" cy="14" rx="3.2" ry="7.5" fill="none" stroke="#fff" stroke-width="1.3"/><path d="M6.5 14h15M8 10h12M8 18h12" stroke="#fff" stroke-width="1.2"/></svg>
    </div>
  </address>
</main>
</body>
</html>
```